Uncle Pim's Tender Biscuits Needs a product label design

We need to design a label for our newly established business - Uncle Pim's Tender Biscuits. This is a start up company that focuses on oatmeal and raisin cookies. I already have a logo designed but need to make the label look very professional and appealing. I would like for the label's background to be white or an off-white. I have to put the ingredients on the front of the label, which I will provide. The cookies are all natural with no preservatives, which is a good selling point and should be on the label. Also, the net weight - 8 ozs and grams - 227 gms, need to be at the very bottom. The final label needs to make folks want to go out and by the cookie. I also need a design that I can change, in case my ingredients change or I want to increase the number of cookies in a bag, which would increase the weight/grams.

I must have 4 set of files for the labels with one word changes in the title and in the ingredients. For example, the label will say:

Label 1 - Uncle Pim's Tender Biscuits
Oatmeal & Raisin

Label 2 - Uncle Pim's Tender Biscuits
Oatmeal & Raisin w/ Chips

Label 3 - Uncle Pim's Tender Biscuits
Oatmeal & Raisin w/ Bits

Label 4 - Uncle Pim's Tender Biscuits
Oatmeal & Raisin Loaded

I have attached my cookie story to give you a feel for how this idea came to life, and I have attached my logos in a few different file formats.

Thanks,
Mi Rena Dobson
555-304-8197

Target Market(s)

Uncle Pim's Tender Biscuits targets all cookie lovers from all age groups and walks of life. Oatmeal & Raisin cookies are all American cookies and all natural, with no preservatives, which will be a big winner for health conscience clients. We will also target the web surfers, hotels, and catering.

Colors
fbed22
acd037
ffc214

Requirements
Must have
• Design must use only the logo attached and the ingredients must be displayed on the front. The Net Weight and Ounces must be displayed on the bottom of the front of the label. The name - Uncle Pim's Tender Biscuits and Oatmeal & Raisin must be displayed on the front.

I must have 4 set of files for the labels with one word change in the title and in the ingredients. For example, the label will say:

Oatmeal & Raisin

Lable 2 - Uncle Pim's Tender Biscuits
Oatmeal & Raisin w/ Chips

Oatmeal & Raisin w/ Bits

Oatmeal & Raisin Loaded
Should not have
• Please use fresh fonts that are eye catching. Only use the logo I have provided.

```html
<!DOCTYPE html>
<html lang="en">
<head>
<meta charset="utf-8">
<title>Uncle Pim's Tender Biscuits – Label Set</title>
<link rel="stylesheet" href="https://fonts.googleapis.com/css2?family=Marcellus&family=Didact+Gothic&family=Varela+Round&display=swap">
<style>
  :root {
    --frame-green: #7cc242;
    --brand-green: #3f9a3a;
    --oval-gold: #fbbf14;
    --banner-gold: #e2b43e;
    --banner-red-dark: #5a0a0c;
    --banner-red: #c8161f;
    --claim-red: #b5271e;
    --band-red: #c9202a;
    --ink: #1a1a1a;
    --paper: #ffffff;
  }
  * { margin: 0; padding: 0; box-sizing: border-box; }
  html, body { width: 1200px; height: 900px; overflow: hidden; background: var(--paper); }
  .canvas { position: relative; width: 1200px; height: 900px; }
  .label-shapes { position: absolute; inset: 0; }
  .brand-name, .brand-tagline, .flavour-banner, .claim, .net-weight { position: absolute; }
  .brand-name {
    font-family: "Marcellus", serif;
    color: var(--brand-green);
    text-align: center;
    line-height: 1.05;
  }
  .brand-tagline {
    font-family: "Marcellus", serif;
    color: var(--brand-green);
    text-align: center;
    letter-spacing: 0.5px;
  }
  .flavour-banner {
    font-family: "Didact Gothic", sans-serif;
    text-align: center;
    box-shadow: 2px 3px 4px rgba(0,0,0,0.35);
  }
  .flavour-banner--loaded {
    left: 160px; top: 415px; width: 280px; height: 33px; line-height: 33px;
    font-size: 17px; color: #fff;
    background: linear-gradient(to right, var(--banner-red), var(--banner-red-dark));
  }
  .flavour-banner--plain {
    left: 733px; top: 362px; width: 219px; height: 24px; line-height: 24px;
    font-size: 14px; color: var(--ink);
    background: var(--banner-gold);
  }
  .claim {
    font-family: "Marcellus", serif;
    color: var(--claim-red);
    white-space: nowrap;
  }
  .net-weight {
    font-family: "Varela Round", sans-serif;
    color: var(--ink);
    white-space: nowrap;
  }
</style>
</head>
<body>
<main class="canvas">
  <svg class="label-shapes" width="1200" height="900" viewBox="0 0 1200 900" aria-hidden="true">
    <defs>
      <filter id="soft-shadow" x="-10%" y="-10%" width="130%" height="140%">
        <feDropShadow dx="2" dy="4" stdDeviation="3" flood-color="#000" flood-opacity="0.3"/>
      </filter>
    </defs>

    <!-- large label -->
    <path class="label-frame" d="M140,128 Q300,108 458,128 A22,22 0 0 0 482,154 L464,806 A22,22 0 0 0 440,830 Q300,850 170,830 A22,22 0 0 0 146,806 L118,154 A22,22 0 0 0 140,128 Z"
          fill="var(--paper)" stroke="var(--frame-green)" stroke-width="6" filter="url(#soft-shadow)"/>
    <ellipse class="claim-oval" cx="300" cy="705" rx="153" ry="57" fill="var(--oval-gold)" filter="url(#soft-shadow)"/>
    <path class="weight-band" d="M182,788 Q300,778 420,786 L416,816 Q300,808 186,818 Z" fill="var(--band-red)" filter="url(#soft-shadow)"/>
    <circle cx="203" cy="802" r="5" fill="var(--ink)"/>
    <rect x="396" y="796" width="12" height="11" fill="#fff"/>
    <circle cx="402" cy="801.5" r="3.5" fill="#2f9a3a"/>

    <!-- small label -->
    <path class="label-frame" d="M718,118 Q840,100 965,118 A20,20 0 0 0 986,142 L970,668 A20,20 0 0 0 950,690 Q840,705 738,690 A20,20 0 0 0 717,668 L698,142 A20,20 0 0 0 718,118 Z"
          fill="var(--paper)" stroke="var(--frame-green)" stroke-width="5" filter="url(#soft-shadow)"/>
    <ellipse class="claim-oval" cx="842" cy="600" rx="120" ry="47" fill="var(--oval-gold)" filter="url(#soft-shadow)"/>
    <path class="weight-band" d="M749,670 Q840,662 936,668 L933,690 Q840,684 752,692 Z" fill="var(--band-red)" filter="url(#soft-shadow)"/>
    <circle cx="765" cy="680" r="4" fill="var(--ink)"/>
    <rect x="917" y="674" width="10" height="9" fill="#fff"/>
    <circle cx="922" cy="678.5" r="3" fill="#2f9a3a"/>
  </svg>

  <!-- large label text -->
  <div class="brand-name" style="left:130px; top:262px; width:340px; font-size:40px;">Uncle Pim's<br>Tender Biscuits</div>
  <div class="brand-tagline" style="left:130px; top:366px; width:340px; font-size:13px;">mouthwateringly delicious</div>
  <div class="flavour-banner flavour-banner--loaded">OATMEAL &amp; RAISIN LOADED</div>
  <div class="claim" style="left:193px; top:672px; font-size:26px;">natural cookies with</div>
  <div class="claim" style="left:170px; top:710px; font-size:26px;">no preservatives</div>
  <div class="net-weight" style="left:216px; top:795px; font-size:11px;">net weight - 8 ozs - 227 gms</div>

  <!-- small label text -->
  <div class="brand-name" style="left:705px; top:242px; width:275px; font-size:32px;">Uncle Pim's<br>Tender Biscuits</div>
  <div class="brand-tagline" style="left:705px; top:320px; width:275px; font-size:11px;">mouthwateringly delicious</div>
  <div class="flavour-banner flavour-banner--plain">OATMEAL &amp; RAISIN</div>
  <div class="claim" style="left:765px; top:574px; font-size:20px;">natural cookies with</div>
  <div class="claim" style="left:740px; top:606px; font-size:20px;">no preservatives</div>
  <div class="net-weight" style="left:776px; top:673px; font-size:9px;">net weight - 8 ozs - 227 gms</div>
</main>
</body>
</html>
```